We have developed a fully functional App called Corvalink. However, it requires a nicer GUI. You can see screenshots of our App on www.corvalink-example.com under "Tutorial". For those of you with Android, you can also install it. When you go to Corvalink-example.com, your phone will automatically redirect you to download. From there, you'll get a better idea of what our App looks like and how your design can make it way better. Please note we expect a design idea for most screens (there's about 8 screens) but do just one screen first and if you win, you can do the other 8 after.

Target Market(s)

People looking for dating / flirting

Industry/Entity Type

Android

Requirements
Must have
• sleek looking

```html
<!DOCTYPE html>
<html lang="en">
<head>
<meta charset="utf-8">
<title>Corvalink – Sign in</title>
<link rel="stylesheet" href="https://fonts.googleapis.com/css2?family=Titillium+Web:wght@300;400;600&display=swap">
<style>
  :root {
    --stage: #c3c3c3;
    --screen-top: #6a2450;
    --screen-mid: #3d1638;
    --screen-bottom: #1d0f2b;
    --ink-light: #ffffff;
    --ink-soft: rgba(255, 255, 255, 0.85);
    --field-bg: #f3f3f3;
    --field-hint: #a9a9a9;
    --accent: #e8a522;
    --social: #3b5a9a;
  }
  * { box-sizing: border-box; margin: 0; padding: 0; }
  html, body {
    width: 1200px;
    height: 900px;
    overflow: hidden;
    background: var(--stage);
    font-family: "Titillium Web", sans-serif;
  }
  .stage {
    width: 1200px;
    height: 900px;
    display: flex;
    align-items: center;
    justify-content: center;
  }
  .login-screen {
    position: relative;
    width: 440px;
    height: 780px;
    background: linear-gradient(200deg, var(--screen-top) 0%, var(--screen-mid) 45%, var(--screen-bottom) 100%);
    color: var(--ink-light);
    overflow: hidden;
  }
  .register-link {
    position: absolute;
    top: 22px;
    right: 24px;
    font-size: 16px;
    font-weight: 300;
    color: var(--ink-soft);
    text-decoration: none;
  }
  .brand {
    position: absolute;
    top: 130px;
    left: 0;
    right: 0;
    display: flex;
    align-items: center;
    justify-content: center;
    gap: 12px;
  }
  .brand-dot {
    width: 14px;
    height: 14px;
    border-radius: 50%;
    background: var(--ink-light);
  }
  .brand-name {
    font-size: 46px;
    font-weight: 300;
    letter-spacing: 0.5px;
    color: var(--ink-light);
  }
  .login-form {
    position: absolute;
    top: 250px;
    left: 60px;
    width: 320px;
    display: flex;
    flex-direction: column;
    align-items: center;
  }
  .field {
    width: 100%;
    height: 42px;
    margin-bottom: 14px;
    padding: 0 14px;
    border: none;
    border-radius: 3px;
    background: var(--field-bg);
    font-family: "Titillium Web", sans-serif;
    font-size: 17px;
    font-weight: 300;
    color: #333;
  }
  .field::placeholder { color: var(--field-hint); }
  .login-button {
    margin-top: 10px;
    width: 180px;
    height: 46px;
    border: none;
    border-radius: 3px;
    background: var(--accent);
    color: var(--ink-light);
    font-family: "Titillium Web", sans-serif;
    font-size: 22px;
    font-weight: 400;
  }
  .forgot-link {
    margin-top: 8px;
    font-size: 12px;
    color: var(--ink-soft);
    text-decoration: none;
  }
  .divider {
    position: absolute;
    top: 470px;
    left: 0;
    right: 0;
    text-align: center;
    font-size: 42px;
    font-weight: 300;
  }
  .social-button {
    position: absolute;
    top: 585px;
    left: 30px;
    width: 380px;
    height: 56px;
    border: none;
    border-radius: 3px;
    background: var(--social);
    color: var(--ink-light);
    font-family: "Titillium Web", sans-serif;
    font-size: 22px;
    font-weight: 400;
  }
</style>
</head>
<body>
  <main class="stage">
    <section class="login-screen">
      <a class="register-link" href="#">Register</a>

      <div class="brand">
        <span class="brand-dot"></span>
        <span class="brand-name">Corvalink</span>
      </div>

      <form class="login-form">
        <input class="field" type="email" placeholder="email -id">
        <input class="field" type="password" placeholder="password">
        <button class="login-button" type="button">Login</button>
        <a class="forgot-link" href="#">Forgot your password ?</a>
      </form>

      <p class="divider">OR</p>

      <button class="social-button" type="button">Connect with Linkbook</button>
    </section>
  </main>
</body>
</html>
```